Female Pest Controller needs awesome business cards

I need a logo design for a Pest Control service - something that appeals to 'nature' & safe, with the use of the colour green. I am also female
New Business Name is 'Bug Bolted'
appeals to women

Target Market(s)

Domestic Households & Local Businesses

Industry/Entity Type

Pest Control

Contact Information for Business Card

Rowena Calderitt
0438526190
ABN 61 847 530 218
PMT7309145538
Spiders Cockroaches, Ants, Silverfish, Fleas, Rodents

Font styles to use
Decorative

Colors
abd036
aaaaaa
5c5c5c

Requirements
Should not have
• Pics of dead insects, prefer nature inspired designs, frogs, trees etc
• Have attached old log & business name ( now my ex's business) Brookhaven Pest Solutions -

```html
<!DOCTYPE html>
<html lang="en">
<head>
<meta charset="UTF-8">
<title>Bug Bolted – Business Cards</title>
<link rel="stylesheet" href="https://fonts.googleapis.com/css2?family=Montserrat:wght@400;500;700;800&display=swap">
<style>
  :root {
    --lime: #b5c93c;
    --lime-mid: #9fb332;
    --lime-deep: #7f9228;
    --forest: #3d6b38;
    --charcoal: #3a3d3a;
    --paper: #ffffff;
    --ink: #2f2f2f;
    --backdrop: #ece9e4;
  }
  * { box-sizing: border-box; margin: 0; padding: 0; }
  html, body { width: 1200px; height: 1200px; overflow: hidden; }
  body {
    background: var(--backdrop);
    font-family: "Montserrat", sans-serif;
    position: relative;
  }
  .card {
    position: absolute;
    width: 580px;
    height: 330px;
    overflow: hidden;
    box-shadow: 0 10px 24px rgba(0,0,0,0.22);
  }
  .card-art { position: absolute; inset: 0; width: 100%; height: 100%; }

  /* front */
  .card-front { left: 70px; top: 70px; }
  .front-brand {
    position: absolute; left: 26px; top: 196px;
    display: flex; align-items: center; gap: 8px;
  }
  .brand-dot { width: 14px; height: 14px; border-radius: 50%; background: var(--lime); flex: none; }
  .brand-name {
    font-weight: 800; color: var(--lime); font-size: 24px; letter-spacing: 0.3px;
    font-family: "Montserrat", sans-serif; white-space: nowrap;
  }
  .name-band {
    position: absolute; left: 300px; top: 80px; width: 280px; height: 68px;
    background: var(--lime); padding: 13px 0 0 34px; color: var(--ink);
  }
  .person-name { font-weight: 700; font-size: 19px; letter-spacing: 2px; line-height: 1.2; }
  .person-role { font-weight: 500; font-size: 14px; margin-top: 1px; }
  .contact-list {
    position: absolute; left: 338px; top: 168px; list-style: none;
    display: flex; flex-direction: column; gap: 12px;
  }
  .contact-item { display: flex; align-items: center; gap: 16px; font-size: 14px; color: var(--ink); letter-spacing: 0.5px; }
  .contact-icon {
    width: 26px; height: 26px; background: var(--lime); flex: none;
    display: flex; align-items: center; justify-content: center;
  }
  .contact-icon.plain { background: none; }

  /* back */
  .card-back { left: 560px; top: 480px; }
  .back-brand {
    position: absolute; left: 0; top: 110px; width: 500px;
    display: flex; justify-content: center; align-items: center; gap: 12px;
  }
  .back-brand .brand-name { font-size: 40px; }
  .back-brand .brand-dot { width: 22px; height: 22px; }
  .back-contacts {
    position: absolute; left: 36px; right: 110px; bottom: 36px;
    display: flex; justify-content: space-between; color: var(--lime); font-size: 14px;
  }
  .back-contact { display: flex; align-items: center; gap: 12px; letter-spacing: 0.5px; }

  /* standalone brand */
  .brand-lockup {
    position: absolute; left: 120px; top: 950px;
    display: flex; align-items: center; gap: 20px;
  }
  .brand-lockup .brand-name { font-size: 78px; color: var(--forest); }
  .brand-lockup .brand-dot { width: 44px; height: 44px; background: var(--lime); }
</style>
</head>
<body>

<section class="card card-front" aria-label="Business card front">
  <svg class="card-art" viewBox="0 0 580 330" preserveAspectRatio="none" aria-hidden="true">
    <rect width="580" height="330" fill="var(--paper)"/>
    <polygon points="0,0 235,0 330,330 0,330" fill="var(--lime)"/>
    <polygon points="0,0 210,0 318,330 0,330" fill="var(--lime-mid)"/>
    <polygon points="0,0 190,0 310,330 0,330" fill="var(--lime-deep)"/>
    <polygon points="0,0 160,0 300,330 0,330" fill="var(--charcoal)"/>
  </svg>
  <div class="front-brand">
    <span class="brand-dot"></span>
    <span class="brand-name">Bug Bolted</span>
  </div>
  <div class="name-band">
    <p class="person-name">YOUR NAME</p>
    <p class="person-role">general manager</p>
  </div>
  <ul class="contact-list">
    <li class="contact-item">
      <span class="contact-icon"><svg width="16" height="16" viewBox="0 0 16 16"><path d="M3 2l3 0 1 3-2 1a8 8 0 0 0 5 5l1-2 3 1 0 3c0 1-1 1-2 1A12 12 0 0 1 2 4c0-1 0-2 1-2z" fill="#fff"/></svg></span>
      <span>333 333 333</span>
    </li>
    <li class="contact-item">
      <span class="contact-icon"><svg width="16" height="12" viewBox="0 0 16 12"><rect x="1" y="1" width="14" height="10" fill="none" stroke="#fff" stroke-width="1.5"/><path d="M1 1l7 6 7-6" fill="none" stroke="#fff" stroke-width="1.5"/></svg></span>
      <span>email@mail.com</span>
    </li>
    <li class="contact-item">
      <span class="contact-icon"><svg width="16" height="16" viewBox="0 0 16 16" fill="none" stroke="#fff" stroke-width="1.2"><circle cx="8" cy="8" r="6.5"/><ellipse cx="8" cy="8" rx="3" ry="6.5"/><path d="M1.5 8h13M2.5 5h11M2.5 11h11"/></svg></span>
      <span>web.www.web.com</span>
    </li>
    <li class="contact-item">
      <span class="contact-icon plain"><svg width="20" height="26" viewBox="0 0 20 26"><path d="M10 1a8 8 0 0 0-8 8c0 6 8 16 8 16s8-10 8-16a8 8 0 0 0-8-8z" fill="var(--lime)"/><circle cx="10" cy="9" r="3" fill="#fff"/></svg></span>
      <span>address street</span>
    </li>
  </ul>
</section>

<section class="card card-back" aria-label="Business card back">
  <svg class="card-art" viewBox="0 0 580 330" preserveAspectRatio="none" aria-hidden="true">
    <rect width="580" height="330" fill="var(--charcoal)"/>
    <polygon points="495,0 520,0 540,330 535,330" fill="var(--lime-deep)"/>
    <polygon points="515,0 545,0 545,330 540,330" fill="var(--lime-mid)"/>
    <polygon points="540,0 580,0 580,40 545,330" fill="var(--lime)"/>
  </svg>
  <div class="back-brand">
    <span class="brand-dot"></span>
    <span class="brand-name">Bug Bolted</span>
  </div>
  <div class="back-contacts">
    <span class="back-contact">
      <svg width="26" height="26" viewBox="0 0 16 16" fill="none" stroke="var(--lime)" stroke-width="1.2"><circle cx="8" cy="8" r="6.5"/><ellipse cx="8" cy="8" rx="3" ry="6.5"/><path d="M1.5 8h13M2.5 5h11M2.5 11h11"/></svg>
      web.www.web.com
    </span>
    <span class="back-contact">
      <svg width="28" height="20" viewBox="0 0 16 12"><rect x="0.5" y="0.5" width="15" height="11" fill="var(--lime)"/><path d="M0.5 0.5l7.5 6 7.5-6" fill="none" stroke="var(--charcoal)" stroke-width="1"/></svg>
      email@email.com
    </span>
  </div>
</section>

<div class="brand-lockup">
  <span class="brand-dot"></span>
  <span class="brand-name">Bug Bolted</span>
</div>

</body>
</html>
```